Redesign of an app landing page

Our page lumvexa.net needs a redesign. This would follow the typical app landing page format which we have now, that is to say a single page with some text, pictures etc. There is also a link to a seperate page with a facebook privacy policy that could use a quick polish.

I want to page to keep the minimamlistic feel that it has now but simply with a better design, a picture that fits the whole screen and the text area similar. You are free to use your design abilities to go outside this preferences if you feel the need to.

The picture in the background should show a social situation which could be anything from taking a lunch, go running, to a museum, the movies, party (no alcohol) or any other situation that we do with our friends. Our logo should be visible as well. If you need any more information, don“t hesitate to take contact

Examples of pages that I like

https://www.quandrel.tv/

http://plorvigo.io/

http://tesmik.co/

Number of Pages Required

1 page

Colors
00a990
0292cd

Requirements
Must have
• The following links need to be there with the correct logos for the pages and the download button should the most visible
• Facebook https://www.example-social.com/lumvexaprogram
• Instagram: https://www.example-photos.com/lum_vexa_kit/
• Play store: https://apps.example-store.com/store/apps/details?id=com.venture.karsido.outingkit
• There needs to be as well the facebook privacy policy link but this can be in small letters somewhere in the corner like it is now.
• http://www.lumvexa.net/#!privacy-policy/qtllt

```html
<!DOCTYPE html>
<html lang="en">
<head>
<meta charset="utf-8">
<title>Lumvexa – Connect you with new people</title>
<link href="https://fonts.googleapis.com/css2?family=Arimo:wght@400;700&display=swap" rel="stylesheet">
<style>
  :root {
    --brand-teal: #00a990;
    --brand-blue: #0292cd;
    --hero-deep: #2b6f92;
    --hero-mid: #3f9fae;
    --hero-light: #6fd0bd;
    --white: #ffffff;
    --phone-body: #1c1c1e;
    --phone-edge: #3a3a3c;
    --screen-top: #8ccfd6;
    --screen-bottom: #0aa9c6;
  }
  * { margin: 0; padding: 0; box-sizing: border-box; }
  html, body { width: 1200px; height: 614px; overflow: hidden; }
  body { font-family: "Arimo", Arial, sans-serif; color: var(--white); }

  .landing { position: relative; width: 1200px; height: 614px; overflow: hidden; }

  .hero-photo {
    position: absolute; inset: 0;
    background:
      radial-gradient(ellipse at 75% 30%, rgba(255,255,255,0.25), transparent 55%),
      linear-gradient(160deg, var(--hero-deep) 0%, var(--hero-mid) 45%, var(--hero-light) 100%);
  }

  .social-links { position: absolute; top: 23px; left: 918px; display: flex; gap: 52px; }
  .social-link { display: flex; flex-direction: column; align-items: center; gap: 6px;
    color: var(--white); text-decoration: none; font-size: 8px; font-weight: 700; width: 52px; }
  .social-link .mark { width: 24px; height: 24px; background: var(--white); }

  .phone {
    position: absolute; left: 33px; top: 207px; width: 285px; height: 440px;
    background: var(--phone-body); border: 3px solid var(--phone-edge); border-radius: 30px;
  }
  .phone .camera { position: absolute; left: 134px; top: 20px; width: 14px; height: 14px;
    border-radius: 50%; background: #0c0c0c; border: 2px solid #2d2d2f; }
  .phone .sensor { position: absolute; left: 41px; top: 24px; width: 6px; height: 6px;
    border-radius: 50%; background: #2a2a4a; }
  .phone-screen {
    position: absolute; left: 9px; top: 44px; width: 261px; height: 400px;
    background: linear-gradient(180deg, var(--screen-top), var(--screen-bottom));
    display: flex; flex-direction: column; align-items: center;
  }
  .phone-screen .brand-dot { margin-top: 56px; width: 132px; height: 132px;
    border: 5px solid var(--white); border-radius: 50%; }
  .phone-screen .welcome { margin-top: 70px; font-size: 34px; font-weight: 700; line-height: 1.1; text-align: center; }

  .hero-copy { position: absolute; left: 560px; top: 266px; width: 514px; text-align: center; }
  .hero-copy h1 { font-size: 31px; font-weight: 700; line-height: 40px; }
  .hero-copy p { margin-top: 34px; font-size: 13px; font-weight: 700; line-height: 25.6px; }

  .download { position: absolute; left: 747px; top: 546px; display: flex; align-items: center; gap: 10px; }
  .download-button {
    display: block; width: 144px; height: 44px; line-height: 44px; border-radius: 4px;
    background: var(--white); color: var(--brand-teal); text-align: center;
    font-size: 18px; font-weight: 700; text-decoration: none;
  }
  .download .store-mark { width: 16px; height: 18px; background: var(--white); }

  .privacy-link { position: absolute; right: 6px; bottom: 2px; font-size: 14px; font-weight: 700;
    color: var(--white); text-decoration: underline; }
</style>
</head>
<body>
<main class="landing">
  <div class="hero-photo" role="img" aria-label="Friends walking together along a snowy forest path, tinted in teal and blue"></div>

  <nav class="social-links">
    <a class="social-link" href="https://www.example-social.com/lumvexaprogram"><span class="mark"></span>Lumvexa</a>
    <a class="social-link" href="https://www.example-photos.com/lum_vexa_kit/"><span class="mark"></span>lum_vexa_kit</a>
  </nav>

  <div class="phone" aria-hidden="true">
    <span class="sensor"></span>
    <span class="camera"></span>
    <div class="phone-screen">
      <span class="brand-dot"></span>
      <div class="welcome">Welcome to<br>lumvexa</div>
    </div>
  </div>

  <section class="hero-copy">
    <h1>Connect you with new people</h1>
    <p>Lumvexa is a free app that connects you with new<br>
    people and allows you to grow your social network.<br>
    Lumvexa lets you&nbsp; publish any activity you want to the<br>
    community and connect with liked-minded people.<br>
    You can also browse through posted activities<br>
    and join the ones you like.</p>
  </section>

  <div class="download">
    <a class="download-button" href="https://apps.example-store.com/store/apps/details?id=com.venture.karsido.outingkit">Download Now</a>
    <span class="store-mark"></span>
  </div>

  <a class="privacy-link" href="http://www.lumvexa.net/#!privacy-policy/qtllt">Privacy policy</a>
</main>
</body>
</html>
```